Startup Drone Platform Company business card

We are needing a business card design for our employees. We are a startup drone platform. We are looking for a business card that has our logo on one side, with the employee/company details on the opposite side. We are looking for something that is very eye catching, modern, and bold.

Target Market(s)

This will target both drone pilots and drone businesses, along with all the industries that could utilize drone services (aerial video, aerial photos, inspections, 3d mapping, etc).

Industry/Entity Type

Business

```html
<!DOCTYPE html>
<html lang="en">
<head>
<meta charset="utf-8">
<title>Skylet Hire – Business Card</title>
<link rel="stylesheet" href="https://fonts.googleapis.com/css2?family=Questrial&display=swap">
<style>
  :root {
    --backdrop: #5b4a3c;
    --card-white: #ffffff;
    --brand-teal: #3fbcc8;
    --ink: #111111;
    --ink-soft: #4a4a4a;
    --rule: #1a1a1a;
  }
  * { margin: 0; padding: 0; box-sizing: border-box; }
  html, body {
    width: 1200px; height: 987px; overflow: hidden;
    background: var(--backdrop);
    font-family: "Questrial", "Century Gothic", sans-serif;
  }
  .card {
    position: absolute; left: 293px; width: 615px; height: 352px;
    box-shadow: 0 3px 8px rgba(0,0,0,0.35);
    overflow: hidden;
  }
  .card-front { top: 125px; background: var(--card-white); }
  .card-back { top: 510px; background: var(--brand-teal); }

  .wordmark {
    position: absolute; right: 39px; top: 50px;
    display: flex; align-items: center; gap: 12px;
    font-size: 23px; letter-spacing: 7px; color: var(--ink);
    margin-right: -7px;
  }
  .wordmark-dot {
    width: 14px; height: 14px; border-radius: 50%;
    background: var(--brand-teal);
  }

  .person-name {
    position: absolute; left: 32px; top: 180px;
    font-size: 26px; color: var(--brand-teal);
  }
  .person-role {
    position: absolute; left: 32px; top: 214px; right: 39px;
    display: flex; align-items: flex-end;
    font-size: 17px; color: var(--ink);
  }
  .person-role .rule {
    flex: 1; height: 1px; background: var(--rule); margin-bottom: 5px;
  }

  .contact-list {
    position: absolute; left: 32px; top: 247px;
    list-style: none; font-size: 16px; color: var(--ink-soft);
  }
  .contact-list li {
    display: flex; align-items: center; gap: 8px; height: 23.5px;
  }
  .contact-list svg { width: 14px; height: 14px; fill: var(--brand-teal); }

  .address-block {
    position: absolute; right: 39px; top: 250px;
    text-align: right; font-size: 16px; line-height: 23.5px; color: var(--ink-soft);
  }

  .edge-band { position: absolute; left: 0; bottom: 0; width: 615px; height: 11px; }

  .back-wordmark {
    position: absolute; left: 0; right: 0; top: 150px;
    display: flex; justify-content: center; align-items: center; gap: 16px;
    font-size: 34px; letter-spacing: 9px; color: var(--card-white);
  }
  .back-wordmark-dot {
    width: 20px; height: 20px; border-radius: 50%;
    border: 3px solid var(--card-white);
  }
  .back-url {
    position: absolute; left: 0; right: 0; top: 302px;
    text-align: center; font-size: 17px; letter-spacing: 3.5px;
    color: var(--card-white);
  }
</style>
</head>
<body>
  <section class="card card-front">
    <div class="wordmark"><span class="wordmark-dot"></span><span>SKYLET HIRE</span></div>

    <h1 class="person-name">Mara Quill</h1>
    <p class="person-role"><span>CEO/Founder</span><span class="rule"></span></p>

    <ul class="contact-list">
      <li>
        <svg viewBox="0 0 24 24" aria-hidden="true"><path d="M6.6 10.8a15.2 15.2 0 0 0 6.6 6.6l2.2-2.2c.3-.3.7-.4 1-.2 1.1.4 2.3.6 3.6.6.6 0 1 .4 1 1V20c0 .6-.4 1-1 1A17 17 0 0 1 3 4c0-.6.4-1 1-1h3.5c.6 0 1 .4 1 1 0 1.3.2 2.5.6 3.6.1.3 0 .7-.2 1z"/></svg>
        <span>555 014 2290</span>
      </li>
      <li>
        <svg viewBox="0 0 24 24" aria-hidden="true"><path d="M7 1h10a2 2 0 0 1 2 2v18a2 2 0 0 1-2 2H7a2 2 0 0 1-2-2V3a2 2 0 0 1 2-2zm0 3v14h10V4zm5 15.5a1.2 1.2 0 1 0 0 2.4 1.2 1.2 0 0 0 0-2.4z"/></svg>
        <span>555 017 3381</span>
      </li>
      <li>
        <svg viewBox="0 0 24 24" aria-hidden="true"><path d="M2 5h20v14H2zm2 2v.5l8 5 8-5V7zm0 2.8V17h16V9.8l-8 5z"/></svg>
        <span>hello@skylethire.com</span>
      </li>
    </ul>

    <address class="address-block" style="font-style:normal">
      4120 Larkspur Way<br>
      Juneau, Alaska 99801<br>
      www.skylethire.com
    </address>

    <svg class="edge-band" viewBox="0 0 615 11" preserveAspectRatio="none" aria-hidden="true">
      <rect x="0" y="0" width="402" height="11" fill="var(--brand-teal)"/>
      <polygon points="406,11 409,0 615,0 615,11" fill="var(--ink)"/>
    </svg>
  </section>

  <section class="card card-back">
    <div class="back-wordmark"><span class="back-wordmark-dot"></span><span>SKYLET HIRE</span></div>
    <p class="back-url">www.skylethire.com</p>
  </section>
</body>
</html>
```